Darrow Consulting needs a quality & professional business card!

I am a recruitment and employment consultant from Brisbane, Australia and I had a fantastic logo organised by this community to I am hoping the business card will be the same.

I have attached the Darrow consulting logo that ideally would feature on the back of the business card. There are a number of logos for you to use as you see fit. I would like the colour cheme to match that of the Darrow Consulting logo. I also have a secondary company called Career Lantern Australia and I have included that logo as well. While it is an important part of the business I don't want this logo feature too predominantly as I am moving out of this space. This logo was created by myself and is of low quality. Feel free to use the icon and words however you want. The winning design will be smart, professional and eye-catching.

The information I am looking for in the business card is:
Name: Gavin Darrow
Position: Founder & Director
Phone: (07) 3519 6482
Mobile: 0431 586 207
Email: gavin@careerlantern.com.au

Target Market(s)

Recruiters, government, large companies

Contact Information for Business Card

Name: Gavin Darrow
Phone: (07) 3519 6482
Mobile: 0431 586 207
Web: www.careerlantern.com.au

Font styles to use
Serif
Sans Serif

Requirements
Must have
• Darrow Consulting Logo on reverse side
• Contact details on front side with smaller reference to Darrow Consulting logo and Career Lantern Australia logo

```html
<!DOCTYPE html>
<html lang="en">
<head>
<meta charset="utf-8">
<title>Darrow Consulting – Business Card</title>
<link href="https://fonts.googleapis.com/css2?family=Raleway:wght@300;400;500&family=Merriweather:wght@700&display=swap" rel="stylesheet">
<style>
  :root {
    --stage: #2b2b2d;
    --card-dark: #1f2124;
    --card-light: #f4f4f4;
    --ink-light: #d9d9d9;
    --ink-muted: #9a9da1;
    --ink-dark: #333538;
    --tab-grey: #5c5f63;
    --accent-blue: #2a8fd0;
    --accent-green: #2d9a48;
    --accent-orange: #e08a2a;
  }
  * { box-sizing: border-box; margin: 0; padding: 0; }
  html, body { width: 1200px; height: 997px; overflow: hidden; }
  body {
    background: var(--stage);
    font-family: "Raleway", Arial, sans-serif;
    position: relative;
  }
  .card {
    position: absolute;
    width: 560px;
    height: 320px;
    border-radius: 3px;
    box-shadow: 0 14px 30px rgba(0,0,0,.45);
    overflow: hidden;
  }
  /* Front side */
  .card-front { left: 70px; top: 140px; display: flex; }
  .front-brand {
    width: 240px;
    background: var(--card-light);
    display: flex;
    flex-direction: column;
    justify-content: space-between;
    padding: 70px 26px 44px;
  }
  .brand-name {
    display: flex; align-items: center; gap: 10px;
    color: var(--ink-dark);
    font-weight: 500;
    letter-spacing: 2px;
    text-transform: uppercase;
  }
  .brand-name .mark { width: 14px; height: 14px; background: var(--ink-dark); flex: none; }
  .brand-name.primary { font-size: 17px; line-height: 1.15; }
  .partner-name {
    display: flex; align-items: center; gap: 10px;
    font-family: "Merriweather", Georgia, serif;
    font-weight: 700;
    font-size: 15px;
    color: var(--ink-dark);
  }
  .partner-name .dot { width: 26px; height: 26px; border-radius: 50%; background: var(--ink-dark); flex: none; }
  .front-details {
    flex: 1;
    background: var(--card-dark);
    position: relative;
    padding: 56px 30px 0 74px;
    color: var(--ink-light);
  }
  .person-name { font-size: 19px; font-weight: 400; letter-spacing: 1px; text-transform: uppercase; }
  .person-role { font-size: 13px; color: var(--ink-muted); margin-top: 4px; }
  .contact-tab {
    position: absolute; left: 0; top: 150px;
    width: 44px; height: 96px;
    background: var(--tab-grey);
    display: flex; flex-direction: column; justify-content: space-around; align-items: center;
    padding: 6px 0;
  }
  .contact-tab svg { width: 16px; height: 16px; }
  .contact-list { list-style: none; position: absolute; left: 74px; top: 152px; font-size: 13px; color: var(--ink-light); font-weight: 300; }
  .contact-list li { height: 30px; line-height: 30px; }
  /* Back side */
  .card-back {
    left: 570px; top: 470px;
    background: var(--card-dark);
    display: flex; align-items: center; justify-content: center;
  }
  .back-brand { display: flex; align-items: center; gap: 18px; }
  .back-brand .mark { width: 30px; height: 30px; background: var(--ink-light); }
  .back-brand .words { color: var(--ink-light); font-weight: 500; letter-spacing: 5px; text-transform: uppercase; font-size: 30px; line-height: 1.1; }
</style>
</head>
<body>
  <section class="card card-front" aria-label="Business card front">
    <div class="front-brand">
      <div class="brand-name primary"><span class="mark"></span><span>Darrow<br>Consulting</span></div>
      <div class="partner-name"><span class="dot"></span><span>Career Lantern<br>Australia</span></div>
    </div>
    <div class="front-details">
      <h1 class="person-name">Gavin Darrow</h1>
      <p class="person-role">Founder &amp; Director</p>
      <div class="contact-tab">
        <svg viewBox="0 0 16 16" aria-label="Phone"><path d="M3 2h3l1 3-2 1a8 8 0 0 0 5 5l1-2 3 1v3a1 1 0 0 1-1 1A12 12 0 0 1 2 3a1 1 0 0 1 1-1z" fill="#e8e8e8"/></svg>
        <svg viewBox="0 0 16 16" aria-label="Mobile"><rect x="4.5" y="1.5" width="7" height="13" rx="1" fill="none" stroke="#e8e8e8"/><circle cx="8" cy="12.5" r=".8" fill="#e8e8e8"/></svg>
        <svg viewBox="0 0 16 16" aria-label="Email"><rect x="1.5" y="3.5" width="13" height="9" fill="none" stroke="#e8e8e8"/><path d="M1.5 3.5 8 9l6.5-5.5" fill="none" stroke="#e8e8e8"/></svg>
      </div>
      <ul class="contact-list">
        <li>(07) 3519 6482</li>
        <li>0431 586 207</li>
        <li>gavin@careerlantern.com.au</li>
      </ul>
    </div>
  </section>

  <section class="card card-back" aria-label="Business card back">
    <div class="back-brand">
      <span class="mark"></span>
      <span class="words">Darrow<br>Consulting</span>
    </div>
  </section>
</body>
</html>
```